VitaLern
Lifeline Instruction
Simple
Ted Marwick
Owner
287 Felcourt Lane Manahawkin, New Jersey 08050
Ted@VitaLern.com
www.VitaLern.com
Healthcare education and consulting.

```html
<!DOCTYPE html>
<html lang="en">
<head>
<meta charset="utf-8">
<title>VitaLern Business Card</title>
<link rel="stylesheet" href="https://fonts.googleapis.com/css2?family=Roboto+Slab:wght@400;700&family=Roboto:wght@400;500&display=swap">
<style>
  :root {
    --page: #e6e6e7;
    --card: #ffffff;
    --red: #e2423c;
    --red-soft: #e85a50;
    --red-dark: #8e1d1c;
    --ink: #555a60;
    --ink-soft: #8a8e93;
    --rule: #d6d6d6;
  }
  * { margin: 0; padding: 0; box-sizing: border-box; }
  html, body { width: 1200px; height: 901px; overflow: hidden; }
  body {
    background: var(--page);
    font-family: "Roboto", Arial, sans-serif;
    position: relative;
  }
  .card {
    position: absolute;
    left: 300px;
    width: 603px;
    height: 342px;
    border-radius: 22px;
    overflow: hidden;
    box-shadow: 0 14px 26px rgba(0,0,0,0.22);
  }
  .card-back { top: 66px; background: var(--red); }
  .card-front { top: 484px; background: var(--card); }

  .back-pattern {
    position: absolute; inset: 0;
    background: linear-gradient(160deg, var(--red-soft), var(--red));
  }
  .back-name {
    position: absolute; left: 352px; top: 248px;
    font-family: "Roboto Slab", Georgia, serif;
    font-weight: 700; font-size: 20px; color: #fff;
  }
  .back-tagline {
    position: absolute; left: 65px; top: 272px;
    font-family: "Roboto Slab", Georgia, serif;
    font-weight: 700; font-size: 15px; color: #fff;
  }

  .brand { position: absolute; left: 34px; top: 147px; display: flex; align-items: center; gap: 10px; }
  .brand-mark { width: 60px; height: 60px; background: var(--red); border-radius: 6px; flex: none; }
  .brand-name { font-size: 28px; font-weight: 400; color: var(--red); line-height: 1; }
  .brand-tagline { font-size: 15px; color: var(--red); margin-top: 3px; }

  .divider {
    position: absolute; left: 301px; top: 76px;
    width: 1px; height: 195px; background: var(--rule);
  }
  .person { position: absolute; left: 321px; top: 64px; }
  .person-name {
    font-family: "Roboto Slab", Georgia, serif;
    font-weight: 400; font-size: 25px; line-height: 30px; color: var(--red); letter-spacing: 0.5px;
  }
  .person-role { font-size: 12px; color: var(--ink-soft); margin-top: 2px; }
  .address {
    position: absolute; left: 321px; top: 138px;
    font-size: 13px; line-height: 20px; color: var(--ink);
  }
  .contacts {
    position: absolute; left: 321px; top: 196px;
    list-style: none; font-size: 13px; color: var(--ink);
  }
  .contacts li { display: flex; align-items: center; height: 19.5px; }
  .contacts svg { width: 10px; height: 10px; margin-right: 9px; fill: var(--red); }
  .wave { position: absolute; left: 0; bottom: 0; width: 603px; height: 70px; }
</style>
</head>
<body>
  <section class="card card-back">
    <div class="back-pattern" role="img" aria-label="Repeating tone-on-tone red pattern"></div>
    <p class="back-name">VitaLern</p>
    <p class="back-tagline">Healthcare Education and Consulting...</p>
  </section>

  <section class="card card-front">
    <div class="brand">
      <span class="brand-mark"></span>
      <div>
        <p class="brand-name">VitaLern</p>
        <p class="brand-tagline">Lifeline Instruction</p>
      </div>
    </div>
    <div class="divider"></div>
    <div class="person">
      <h1 class="person-name">TED MARWICK</h1>
      <p class="person-role">Owner</p>
    </div>
    <p class="address">287 Felcourt Lane Westbrook Hollow,<br>Ohio 44999</p>
    <ul class="contacts">
      <li><svg viewBox="0 0 10 10"><path d="M2 0.5 L3.8 2.6 L2.9 3.8 Q4 6 6.2 7.1 L7.4 6.2 L9.5 8 L8.3 9.5 Q3.5 9 0.5 1.7 Z"/></svg>732-555-0147</li>
      <li><svg viewBox="0 0 10 10"><path d="M2.5 0 H7.5 V10 H2.5 Z M3.3 1 V8 H6.7 V1 Z" fill-rule="evenodd"/></svg>732-555-0182</li>
      <li><svg viewBox="0 0 10 10"><path d="M0 2 H10 V8.5 H0 Z M0.6 2.4 L5 5.6 L9.4 2.4 Z" fill-rule="evenodd"/></svg>Ted@VitaLern.com</li>
      <li><svg viewBox="0 0 10 10"><circle cx="5" cy="5" r="4.6"/></svg>www.VitaLern.com</li>
    </ul>
    <svg class="wave" viewBox="0 0 603 70" preserveAspectRatio="none">
      <path d="M0 40 C150 10 320 5 603 22 L603 70 L0 70 Z" fill="#f1c9c6"/>
      <path d="M0 48 C170 18 340 12 603 30 L603 70 L0 70 Z" fill="var(--red-dark)"/>
      <path d="M0 56 C180 32 360 28 603 42 L603 70 L0 70 Z" fill="#a5262a"/>
    </svg>
  </section>
</body>
</html>
```